Flyer for Car Detailing Shop

I am opening a detailing shop. I am looking for a nice, easy to read single sided flyer I can hand out at car shows, hang in store windows and to my clients and customers to promote my business. I want it a little professional yet attention grabbing. I want someone to look at it and go "holy shit, thats a nice flyer" haha

Here are some things that must be included:
- Company Name: Brightfern Motorworks Detailing & Coatings
- Tag Line: The Science of Detailing
- Address: 4150 Harlow Rd, Temperance, MI 48190
- www.brightfernmotor.example
- Find Us on social Media! ::insert facebook and instagram logo
Colors: Black, Lime Green and Purple for accents, etc

HAND WASH
- Express Wash start at $25
- Deluxe Wash Start at $50

EXTERIOR DETAILING
-Basic Packages Start at $160
- Deluxe Packages Start at $350

INTERIOR DETAILING
- Basic Packages Start at $60
- Deluxe Packages Start at $200

New Car Prep and Ceramic Coatings
*Consultation required prior to beginning work*
- Paint: Starting at $500
- Interior: Starting at $100
- Wheels Off: Starting at $200
- Trim: Starting at $100
- Windows: $50 windshield/ $25 per pane

Additional Services
- Scratch removal
- Ozone Treatment
- Headlight Restoration
- Chip Repair

```html
<!DOCTYPE html>
<html lang="en">
<head>
<meta charset="utf-8">
<title>Brightfern Motorworks – Flyer</title>
<link href="https://fonts.googleapis.com/css2?family=Poppins:wght@400;500;600;700;800&family=Karla:wght@400&family=Oswald:wght@400&display=swap" rel="stylesheet">
<style>
  :root{
    --bg:#ececec;
    --paper:#ffffff;
    --ink:#111111;
    --muted:#5a5a5a;
    --green:#3dba68;
    --green-soft:#bfe6cb;
    --night:#1f1d27;
    --garage:#2e2d33;
  }
  *{box-sizing:border-box;margin:0;padding:0}
  html,body{width:1200px;height:1200px;overflow:hidden;background:var(--bg)}
  .flyer{position:absolute;left:180px;top:12px;width:839px;height:1176px;background:var(--paper);overflow:hidden}
  .backdrop{position:absolute;inset:0}
  .abs{position:absolute}
  .headline{left:55px;top:62px;font:700 41px/46px "Poppins",sans-serif;color:#fff;letter-spacing:-0.5px}
  .accent{color:var(--green)}
  .car-photo{position:absolute;left:79px;top:150px;width:722px;height:365px}
  .section-title{font:800 24px/30px "Poppins",sans-serif;color:var(--ink);letter-spacing:-0.2px}
  .rule{height:2px;background:var(--green)}
  .consult-note{font:500 12px/14px "Poppins",sans-serif;color:var(--muted);letter-spacing:0.2px}
  .row{position:absolute;height:28px;display:flex;align-items:center;justify-content:space-between}
  .row .label{font:400 17px "Karla",sans-serif;color:var(--muted);letter-spacing:0.6px}
  .price{width:74px;height:28px;background:var(--green);color:#fff;font:700 15px/28px "Poppins",sans-serif;text-align:right;padding-right:12px}
  .col-left .row{left:55px;width:341px}
  .col-right .row{left:439px;width:344px}
  .extra{position:absolute;display:flex;align-items:center;gap:12px}
  .extra .num{width:44px;font:400 46px/1 "Oswald",sans-serif;color:var(--green-soft)}
  .extra .name{font:400 17px/22px "Karla",sans-serif;color:var(--muted);letter-spacing:0.6px}
  .brand{left:16px;top:1068px;width:280px;text-align:center;font:600 15px/21px "Poppins",sans-serif;color:#fff;letter-spacing:1px}
  .brand-dot{left:131px;top:1000px;width:50px;height:50px;border-radius:50%;background:var(--green)}
  .footer-tag{left:351px;top:1060px;font:700 24px/30px "Poppins",sans-serif;color:#fff}
  .contact{left:534px;top:1057px;font:500 13px/17px "Poppins",sans-serif;color:#fff;letter-spacing:0.4px;font-style:normal}
  .contact .web{margin-top:4px}
  .social-note{left:352px;top:1133px;font:400 13px "Poppins",sans-serif;color:var(--green)}
</style>
</head>
<body>
<div class="flyer">
  <svg class="backdrop" width="839" height="1176" viewBox="0 0 839 1176">
    <polygon points="0,0 839,0 839,472 0,266" fill="var(--garage)"/>
    <polygon points="0,266 839,472 839,511 0,290" fill="var(--green)"/>
    <polygon points="492,0 839,0 839,91" fill="var(--green)"/>
    <polygon points="560,0 839,0 839,72" fill="var(--paper)"/>
    <path d="M0,926 L280,926 C330,926 352,952 382,988 C402,1012 420,1018 450,1018 L839,1018 L839,1176 L0,1176Z" fill="var(--green)"/>
    <path d="M0,936 L280,936 C326,936 346,962 374,996 C396,1022 416,1028 450,1028 L839,1028 L839,1176 L0,1176Z" fill="var(--night)"/>
    <line x1="534" y1="1146" x2="737" y2="1146" stroke="var(--green)" stroke-width="1.5"/>
    <polygon points="742,1128 760,1128 754,1146 736,1146" fill="var(--green)"/>
    <polygon points="765,1128 783,1128 777,1146 759,1146" fill="var(--green)"/>
  </svg>

  <svg class="car-photo" role="img" aria-label="Glossy red sports car, front three-quarter view" viewBox="0 0 722 365" preserveAspectRatio="none">
    <defs>
      <radialGradient id="carTone" cx="48%" cy="50%" r="55%">
        <stop offset="0" stop-color="#d0283c"/>
        <stop offset="0.7" stop-color="#9c1426"/>
        <stop offset="1" stop-color="#5a0c16" stop-opacity="0"/>
      </radialGradient>
    </defs>
    <ellipse cx="361" cy="190" rx="360" ry="172" fill="url(#carTone)"/>
  </svg>

  <h1 class="abs headline">The <span class="accent">Science</span><br>of Detailing</h1>

  <div class="col-left">
    <h2 class="abs section-title" style="left:55px;top:521px">HAND WASH</h2>
    <div class="abs rule" style="left:55px;top:551px;width:341px"></div>
    <div class="row" style="top:562px"><span class="label">Express Wash start at</span><span class="price">$25</span></div>
    <div class="row" style="top:593px"><span class="label">Deluxe Wash Start at</span><span class="price">$50</span></div>

    <h2 class="abs section-title" style="left:55px;top:655px">EXTERIOR DETAILING</h2>
    <div class="abs rule" style="left:55px;top:684px;width:341px"></div>
    <div class="row" style="top:696px"><span class="label">Basic Packages Start at</span><span class="price">$160</span></div>
    <div class="row" style="top:726px"><span class="label">Deluxe Packages Start at</span><span class="price">$350</span></div>

    <h2 class="abs section-title" style="left:55px;top:785px">INTERIOR DETAILING</h2>
    <div class="abs rule" style="left:55px;top:814px;width:341px"></div>
    <div class="row" style="top:825px"><span class="label">Basic Packages Start at</span><span class="price">$60</span></div>
    <div class="row" style="top:855px"><span class="label">Deluxe Packages Start at</span><span class="price">$200</span></div>
  </div>

  <div class="col-right">
    <h2 class="abs section-title" style="left:439px;top:526px">NEW CAR PREP<br>AND CERAMIC COATINGS</h2>
    <div class="abs rule" style="left:439px;top:586px;width:344px"></div>
    <p class="abs consult-note" style="left:439px;top:593px">*Consultation required prior to beginning work*</p>
    <div class="row" style="top:613px"><span class="label">Paint: Starting at</span><span class="price">$500</span></div>
    <div class="row" style="top:642px"><span class="label">Interior: Starting at</span><span class="price">$100</span></div>
    <div class="row" style="top:671px"><span class="label">Wheels Off: Starting at</span><span class="price">$200</span></div>
    <div class="row" style="top:700px"><span class="label">Trim: Starting at</span><span class="price">$100</span></div>
    <div class="row" style="top:729px"><span class="label">Windows: windshield</span><span class="price">$50</span></div>
    <div class="row" style="top:758px"><span class="label">Windows: per pane</span><span class="price">$25</span></div>

    <h2 class="abs section-title" style="left:439px;top:810px">Additional Services</h2>
    <div class="abs rule" style="left:439px;top:840px;width:344px"></div>
    <div class="extra" style="left:439px;top:865px"><span class="num">01</span><span class="name">Scratch<br>Removal</span></div>
    <div class="extra" style="left:620px;top:865px"><span class="num">02</span><span class="name">Ozone<br>Treatment</span></div>
    <div class="extra" style="left:439px;top:935px"><span class="num">03</span><span class="name">Headlight<br>Restoration</span></div>
    <div class="extra" style="left:620px;top:935px"><span class="num">04</span><span class="name">Chip<br>Repair</span></div>
  </div>

  <div class="abs brand-dot"></div>
  <div class="abs brand">BRIGHTFERN MOTORWORKS<br>DETAILING &amp; COATINGS</div>

  <p class="abs footer-tag">The <span class="accent">Science</span><br>of Detailing</p>
  <address class="abs contact">
    4150 Harlow Rd,<br>Temperance, MI 48190
    <div class="web">www.brightfernmotor.example</div>
  </address>
  <p class="abs social-note">Find us on social media</p>
</div>
</body>
</html>
```